Moderne CI für einen Immobilienmakler [www.terbek-wohnwerte.de]
Zielgruppe
Kunden für hochwertige Immobilien, also gemischtes eher anspruchvolles Klientel.
Hallo,
ich betreibe ein junges Immobilienunternehmen im 4. Geschäftsjahr. Wir vermarkten ausschließlich hochwertige Immobilien. Meine derzeitiges Logo habe ich damals selbst entworfen und es harmoniert gut mit meiner Website [www.terbek-wohnwerte.de] leider habe ich für Printmedien nie eine CI hinbekommen die mir richtig gefällt und die im Gesamt- und Farbkonzept zu meinem Onlineauftritt passt.
Ich wünsche mir nun von einem professionellen Designer eine modern- edle CI mit Entwürfen für Briefpapier, Umschläge C4 und DL, A4 Exposé-Mappe sowie die Rohlinge für eine Dreiseiter Image-Broschüre, für ein Objekt Expose sowie für eine Print-Annonce.
Eine spätere Zusammenarbeit für weitere Medien ist erwünscht.

```html
<!DOCTYPE html>
<html lang="de">
<head>
<meta charset="utf-8">
<title>terbek wohnwerte – Visitenkarte</title>
<link rel="stylesheet" href="https://fonts.googleapis.com/css2?family=Open+Sans:wght@400;600&display=swap">
<style>
  :root {
    --bg: #ececec;
    --white: #ffffff;
    --red-dark: #bf0000;
    --red-light: #f00000;
    --ink: #1a1a1a;
    --grey: #777777;
    --rule: #b5b5b5;
  }
  * { margin: 0; padding: 0; box-sizing: border-box; }
  html, body {
    width: 1200px; height: 1200px; overflow: hidden;
    background: var(--bg);
    font-family: "Open Sans", Arial, sans-serif;
  }
  .sheet { position: relative; width: 1200px; height: 1200px; }
  .card {
    position: absolute; left: 260px;
    width: 680px; height: 440px;
    overflow: hidden;
  }
  .card--front { top: 130px; background: var(--white); }
  .card--back {
    top: 630px;
    background: linear-gradient(90deg, var(--red-dark), var(--red-light));
  }

  /* front */
  .brand {
    position: absolute; right: 40px; top: 48px;
    font-size: 36px; font-weight: 600; color: var(--ink);
  }
  .person { position: absolute; left: 316px; top: 150px; }
  .person__name { font-size: 30px; font-weight: 400; color: var(--ink); line-height: 1.1; }
  .person__role { font-size: 19px; color: var(--grey); margin-top: 4px; }
  .divider {
    position: absolute; left: 0; right: 0; top: 252px;
    height: 4px; background: var(--rule);
  }
  .band {
    position: absolute; left: 0; right: 0; top: 262px; bottom: 0;
    background: linear-gradient(90deg, var(--red-dark), var(--red-light));
    color: var(--white);
  }
  .address {
    position: absolute; left: 48px; top: 28px;
    font-size: 19px; line-height: 1.45;
  }
  .address__gap { display: block; height: 14px; }
  .online {
    position: absolute; left: 316px; top: 92px;
    font-size: 19px; font-weight: 600; line-height: 1.4;
  }
  .band__square {
    position: absolute; left: 604px; top: 110px;
    width: 26px; height: 26px; background: var(--white);
  }

  /* back */
  .back__square {
    position: absolute; left: 52px; bottom: 66px;
    width: 34px; height: 34px; background: var(--white);
  }
  .back__url {
    position: absolute; left: 124px; bottom: 64px;
    font-size: 20px; font-weight: 600; color: var(--white);
  }
</style>
</head>
<body>
<main class="sheet">
  <section class="card card--front" aria-label="Visitenkarte Vorderseite">
    <p class="brand">terbek wohnwerte</p>
    <div class="person">
      <p class="person__name">Henrik Terbek</p>
      <p class="person__role">Geschäftsführer</p>
    </div>
    <div class="divider"></div>
    <div class="band">
      <p class="address">
        Kastanienweg 12<br>
        D-34117 Kassel
        <span class="address__gap"></span>
        Fon: +49 (0)561 5820314<br>
        Fax: +49 (0)561 5820316
      </p>
      <p class="online">
        www.terbek-wohnwerte.de<br>
        ht@terbek-wohnwerte.de
      </p>
      <span class="band__square"></span>
    </div>
  </section>

  <section class="card card--back" aria-label="Visitenkarte Rückseite">
    <span class="back__square"></span>
    <p class="back__url">www.terbek-wohnwerte.de</p>
  </section>
</main>
</body>
</html>
```